Atlanta housekeeping/cleaning company needs a car wrap design for a 2019 Valdane Orsk Quillon Van

We need a car wrap design for a maid/housekeeping company based in Atlanta, Georgia, called Coralbeck Maids. Our vehicle is a 2019 Valdane Orsk Quillon van with passenger configuration and rear split barn doors. Keep in mind the bumpers cannot be wrapped as they are plastic. I am open to having widows wrapped to provide additional room for the creative design. Our core values are trustworthiness, affordability, quality, thoroughness, and respect. We offer our customers the option to call or book online, so please ensure to relay that in the design. Our company promises to be eco-friendly wherever possible and we need our car wrap design to communicate this to our customers by using the color green. Please don't feel a need to include the "Coralbeck Maids" text just below the logo. Get creative, and include it beside the logo, or somewhere else! I am attaching some designs I found online that I liked.

Target Market(s)

Mid to High end Housekeeping and cleaning services.

Industry/Entity Type

House Cleaning

Requirements
Must have
• Please include our email, care@coralbeckmaids.example, our phone number 1(888) 562-DUSK (3875), and our website, www.coralbeckmaids.example, in your design. Thank you!

```html
<!DOCTYPE html>
<html lang="en">
<head>
<meta charset="utf-8">
<title>Coralbeck Maids – Van Wrap Layouts</title>
<link rel="stylesheet" href="https://fonts.googleapis.com/css2?family=Fredoka:wght@600&family=Poppins:wght@600&display=swap">
<style>
  :root {
    --bg: #e6e7e9;
    --wrap-white: #ffffff;
    --brand-brown: #3d2213;
    --brand-green: #3cb83a;
    --brand-green-light: #7fd65a;
    --sky-blue: #4fc3d9;
    --outline: #c9cbcf;
  }
  * { margin: 0; padding: 0; box-sizing: border-box; }
  html, body { width: 1200px; height: 1200px; overflow: hidden; background: var(--bg); }
  .canvas {
    width: 1200px; height: 1200px;
    display: flex; flex-direction: column; justify-content: center; align-items: center;
    gap: 90px;
  }
  .wrap-layout { width: 1100px; height: 420px; display: block; }
  .panel { fill: var(--wrap-white); stroke: var(--outline); stroke-width: 2; }
  .band-brown { fill: var(--brand-brown); }
  .band-green { fill: var(--brand-green); }
  .swoosh-blue { fill: var(--sky-blue); }
  .brand-name { font-family: "Fredoka", sans-serif; font-weight: 600; fill: var(--brand-brown); }
  .contact { font-family: "Poppins", sans-serif; font-weight: 600; fill: var(--brand-brown); }
  .contact-light { font-family: "Poppins", sans-serif; font-weight: 600; fill: var(--wrap-white); }
  .call-to-action { font-family: "Poppins", sans-serif; font-weight: 600; fill: var(--brand-green); }
  .mark-circle { fill: var(--brand-green-light); stroke: var(--wrap-white); stroke-width: 6; }
  .divider { stroke: var(--brand-green); stroke-width: 3; }
</style>
</head>
<body>
<main class="canvas">

  <!-- Layout A: straight bands -->
  <svg class="wrap-layout" viewBox="0 0 1100 420" aria-label="Coralbeck Maids van wrap, straight band layout">
    <defs>
      <clipPath id="panel-a"><rect x="2" y="2" width="1096" height="416" rx="60"/></clipPath>
    </defs>
    <rect class="panel" x="2" y="2" width="1096" height="416" rx="60"/>
    <g clip-path="url(#panel-a)">
      <rect class="band-green" x="920" y="0" width="180" height="420"/>
      <rect class="band-brown" x="0" y="300" width="1100" height="26"/>
      <rect class="band-green" x="0" y="336" width="1100" height="84"/>
    </g>
    <text class="call-to-action" x="470" y="58" font-size="18">Call or book online</text>
    <text class="contact" x="470" y="92" font-size="24">1(888) 562-DUSK (3875)</text>
    <text class="contact" x="470" y="124" font-size="21">www.coralbeckmaids.example</text>
    <text class="contact" x="470" y="154" font-size="21">care@coralbeckmaids.example</text>
    <text class="brand-name" x="240" y="275" font-size="78">Coralbeck Maids</text>
    <circle class="mark-circle" cx="990" cy="160" r="70"/>
  </svg>

  <!-- Layout B: diagonal bands -->
  <svg class="wrap-layout" viewBox="0 0 1100 420" aria-label="Coralbeck Maids van wrap, diagonal band layout">
    <defs>
      <clipPath id="panel-b"><rect x="2" y="2" width="1096" height="416" rx="60"/></clipPath>
    </defs>
    <rect class="panel" x="2" y="2" width="1096" height="416" rx="60"/>
    <g clip-path="url(#panel-b)">
      <polygon class="swoosh-blue" points="0,190 760,95 0,215"/>
      <polygon class="band-green" points="0,330 1100,180 1100,420 0,420"/>
      <polygon class="band-brown" points="220,340 1100,190 1100,240 220,390"/>
    </g>
    <g transform="rotate(-9.67 220 365)">
      <text class="brand-name" x="235" y="328" font-size="74">Coralbeck Maids</text>
      <text class="contact-light" x="245" y="373" font-size="22">1(888) 562-DUSK (3875)</text>
      <line class="divider" x1="535" y1="353" x2="535" y2="378"/>
      <text class="contact-light" x="555" y="373" font-size="21">www.coralbeckmaids.example</text>
      <text class="contact-light" x="245" y="412" font-size="19">Call or book online · care@coralbeckmaids.example</text>
    </g>
    <circle class="mark-circle" cx="960" cy="120" r="70"/>
  </svg>

</main>
</body>
</html>
```